Pellmore Heating & Air

I need a business card made for my company. I would like my new logo for Pellmore Heating and Air on the front and my Garage Door on the back.
Front to say -Heating & Air Conditioning , Mini Splits and Heat Pumps, Hydronic In-Floor Heat. Locally Owned and Operated! Licensed, Boned and Insured. Free Estimates on new equipment. 555-201-4837
KVB Back Card, change phone# to 555-318-6024. Remove Commercial and residential and fully sticked vans lines.

```html
<!DOCTYPE html>
<html lang="en">
<head>
<meta charset="utf-8">
<title>Pellmore Heating &amp; Air — Business Cards</title>
<link rel="stylesheet" href="https://fonts.googleapis.com/css2?family=Montserrat:wght@400;500;700;800;900&display=swap">
<style>
  :root {
    --brand-blue: #0f5189;
    --brand-red: #e8302a;
    --paper: #ffffff;
    --ink: #1d2b3a;
    --backdrop-top: #d2d2d2;
    --backdrop-bottom: #a9a9a9;
  }
  * { box-sizing: border-box; margin: 0; padding: 0; }
  html, body { width: 1200px; height: 815px; overflow: hidden; }
  body {
    background: linear-gradient(180deg, var(--backdrop-top), var(--backdrop-bottom));
    font-family: "Montserrat", sans-serif;
    display: flex;
    align-items: center;
    justify-content: center;
    gap: 24px;
  }
  .card {
    position: relative;
    width: 560px;
    height: 320px;
    overflow: hidden;
    box-shadow: 0 10px 24px rgba(0,0,0,0.28);
  }

  /* ---------- Garage door card ---------- */
  .card--garage {
    background: var(--paper);
    border-bottom: 4px solid var(--brand-red);
  }
  .garage-brand {
    position: absolute;
    left: 28px;
    top: 62px;
    width: 220px;
    display: flex;
    align-items: center;
    gap: 10px;
  }
  .garage-brand__mark {
    flex: none;
    width: 26px;
    height: 26px;
    border-radius: 50%;
    background: var(--brand-blue);
  }
  .garage-brand__name {
    font-weight: 800;
    font-size: 27px;
    line-height: 1.05;
    text-transform: uppercase;
    color: var(--brand-blue);
  }
  .garage-divider {
    position: absolute;
    left: 262px;
    top: 36px;
    width: 1.5px;
    height: 150px;
    background: var(--brand-red);
  }
  .contact {
    position: absolute;
    left: 286px;
    top: 36px;
    color: var(--ink);
  }
  .contact__name {
    font-weight: 800;
    font-size: 24px;
    letter-spacing: 1px;
    color: var(--brand-blue);
    text-transform: uppercase;
  }
  .contact__role {
    font-size: 13px;
    letter-spacing: 1px;
    margin-top: 2px;
  }
  .contact__rule {
    width: 20px;
    height: 1.5px;
    background: var(--brand-red);
    margin: 14px 0 12px;
  }
  .contact__list { list-style: none; }
  .contact__item {
    display: flex;
    align-items: center;
    gap: 8px;
    font-size: 12.5px;
    line-height: 22px;
  }
  .contact__item svg { width: 11px; height: 11px; flex: none; }
  .service-band {
    position: absolute;
    left: 0;
    right: 0;
    bottom: 30px;
    height: 54px;
    background: var(--brand-red);
    display: flex;
    align-items: center;
    justify-content: center;
    gap: 14px;
    color: var(--paper);
    font-weight: 800;
    text-transform: uppercase;
  }
  .service-band__label { font-size: 19px; letter-spacing: 1px; }
  .service-band__phone { font-size: 24px; letter-spacing: 1px; }
  .service-band__icon {
    width: 46px;
    height: 46px;
    border-radius: 50%;
    background: var(--brand-blue);
    border: 3px solid var(--paper);
    display: flex;
    align-items: center;
    justify-content: center;
  }

  /* ---------- Heating card ---------- */
  .card--heating {
    background: var(--brand-blue);
    border-bottom: 4px solid var(--brand-red);
    color: var(--paper);
  }
  .heating-brand {
    position: absolute;
    left: 0;
    right: 0;
    top: 70px;
    text-align: center;
    font-weight: 900;
    font-size: 42px;
    line-height: 1.05;
    text-transform: uppercase;
    color: var(--paper);
  }
  .services {
    position: absolute;
    left: 24px;
    right: 24px;
    bottom: 42px;
    text-align: center;
    font-weight: 500;
    font-size: 13.5px;
    line-height: 24px;
  }
  .services__dot {
    display: inline-block;
    width: 5px;
    height: 5px;
    border-radius: 50%;
    background: var(--brand-red);
    margin: 0 6px;
    vertical-align: middle;
  }
</style>
</head>
<body>

  <section class="card card--garage" aria-label="Kenvale Garage Door card">
    <div class="garage-brand">
      <span class="garage-brand__mark"></span>
      <span class="garage-brand__name">Kenvale Garage Door</span>
    </div>
    <div class="garage-divider"></div>
    <div class="contact">
      <p class="contact__name">Dalen Ashby</p>
      <p class="contact__role">OWNER</p>
      <div class="contact__rule"></div>
      <ul class="contact__list">
        <li class="contact__item">
          <svg viewBox="0 0 12 12"><path d="M3 1l2 2.5-1.2 1.3a7 7 0 0 0 3.4 3.4L8.5 7 11 9l-1.2 2C5.5 11 1 6.5 1 2.2z" fill="#e8302a"/></svg>
          555-318-6024
        </li>
        <li class="contact__item">
          <svg viewBox="0 0 12 12"><rect x="1" y="2.5" width="10" height="7" fill="#e8302a"/><path d="M1 2.5l5 4 5-4" stroke="#fff" fill="none"/></svg>
          kenvalegaragedoor@example.com
        </li>
        <li class="contact__item">
          <svg viewBox="0 0 12 12"><circle cx="6" cy="6" r="5" fill="#e8302a"/><path d="M1 6h10M6 1c-2.5 3-2.5 7 0 10M6 1c2.5 3 2.5 7 0 10" stroke="#fff" stroke-width=".7" fill="none"/></svg>
          www.kenvalegaragedoor.com
        </li>
      </ul>
    </div>
    <div class="service-band">
      <span class="service-band__label">Free Service Call</span>
      <span class="service-band__icon">
        <svg viewBox="0 0 24 24" width="22" height="22"><path d="M4 15c0-2 3.5-3.5 8-3.5s8 1.5 8 3.5l-2.5 1.5-2-2v-1.5c-2-.6-5-.6-7 0V14l-2 2z" fill="#fff"/><path d="M8 8.5a6 6 0 0 1 8 0M10 10a3 3 0 0 1 4 0" stroke="#fff" stroke-width="1.4" fill="none" stroke-linecap="round"/></svg>
      </span>
      <span class="service-band__phone">555-201-4837</span>
    </div>
  </section>

  <section class="card card--heating" aria-label="Pellmore Heating and Air card">
    <h1 class="heating-brand">Pellmore<br>Heating &amp; Air</h1>
    <p class="services">
      Heating &amp; Air Conditioning<span class="services__dot"></span>Mini Splits and Heat Pumps<span class="services__dot"></span>Hydronic In-Floor Heat<br>
      <span class="services__dot"></span>Locally Owned and Operated!<span class="services__dot"></span>Licensed, Boned and Insured
    </p>
  </section>

</body>
</html>
```